Exciting Personal Development Book Cover: FIND ZEN NOW!

Design a Book Cover for my personal development book.
Title: Find Zen Now!
Author: Marcus Telly
Tagline: A real-life solution to get unstuck and break free

My picture must make up the front cover as I need to build my brand and people should recognise me on book shelves. Bold and catchy. How you do it is up to you. There must be space for a short testimonial from a famous person who is currently reading my book. I uploaded a sample of what I made in Photoshop but I don't have design skills.

I've added a PDF of my book so you can read the chapter index and introduction to get a sense of the content.

Target Market(s)

Personal Development Self-Help Market

Industry/Entity Type

Personal Development

Font styles to use
Serif
Sans Serif

Requirements
Must have
• My picture as hero image on cover.
Nice to have
• Must have Title, Tagline and my author name. If possible ZEN stands for 'Zeal, Energy & Nerve' If there is a way to fit this somewhere great. If it's too much then it can go somewhere on the back.

```html
<!DOCTYPE html>
<html lang="en">
<head>
<meta charset="utf-8">
<title>Find Zen Now! – Marcus Telly</title>
<link href="https://fonts.googleapis.com/css2?family=Federo&family=Cormorant+SC:wght@500&display=swap" rel="stylesheet">
<style>
  :root {
    --bg-top: #a9b4c1;
    --bg-mid: #c3ccd6;
    --bg-bottom: #b4bfcb;
    --ink: #141414;
    --white: #ffffff;
    --shadow: rgba(40, 50, 65, 0.45);
    --photo-light: #d9c2b2;
    --photo-shirt: #f1f1f0;
    --photo-shade: #c9ccd1;
  }
  html, body {
    margin: 0;
    padding: 0;
    overflow: hidden;
  }
  .cover {
    position: relative;
    width: 776px;
    height: 1200px;
    overflow: hidden;
    background: radial-gradient(ellipse at 45% 45%, var(--bg-mid) 0%, var(--bg-top) 65%, var(--bg-bottom) 100%);
    font-family: "Federo", sans-serif;
  }
  .title {
    position: absolute;
    top: 76px;
    left: 0;
    width: 776px;
    margin: 0;
    text-align: center;
    font-weight: 400;
    font-size: 84px;
    line-height: 1;
    letter-spacing: 1px;
    word-spacing: 8px;
    color: var(--ink);
    text-shadow: 4px 6px 7px var(--shadow);
    white-space: nowrap;
  }
  .tagline {
    position: absolute;
    top: 184px;
    left: 0;
    width: 776px;
    margin: 0;
    text-align: center;
    font-family: "Cormorant SC", serif;
    font-weight: 500;
    font-size: 19px;
    letter-spacing: 1.5px;
    color: var(--white);
    text-shadow: 1px 2px 3px var(--shadow);
    text-transform: uppercase;
    white-space: nowrap;
  }
  .hero-photo {
    position: absolute;
    left: 290px;
    top: 292px;
    width: 486px;
    height: 908px;
    border-radius: 46% 46% 0 0 / 16% 16% 0 0;
    background: linear-gradient(180deg, var(--photo-light) 0%, var(--photo-light) 26%, var(--photo-shirt) 34%, var(--photo-shade) 100%);
  }
  .zen-meaning {
    position: absolute;
    left: 48px;
    top: 505px;
    margin: 0;
    padding: 0;
    list-style: none;
    color: var(--white);
    font-size: 50px;
    line-height: 92px;
    letter-spacing: 1px;
    text-shadow: 3px 5px 6px var(--shadow);
  }
  .author {
    position: absolute;
    left: 0;
    bottom: 44px;
    width: 776px;
    margin: 0;
    text-align: center;
    font-weight: 400;
    font-size: 88px;
    line-height: 1;
    letter-spacing: 3px;
    color: var(--white);
    text-shadow: 3px 5px 7px var(--shadow);
    white-space: nowrap;
  }
</style>
</head>
<body>
  <main class="cover">
    <div class="hero-photo" role="img" aria-label="Portrait photograph of the author in a white shirt with tattooed forearms, smiling, arms crossed"></div>
    <h1 class="title">FIND ZEN NOW !</h1>
    <p class="tagline">A real-life solution to get unstuck and break free</p>
    <ul class="zen-meaning">
      <li>ZEAL</li>
      <li>ENERGY</li>
      <li>NERVE</li>
    </ul>
    <p class="author">MARCUS TELLY</p>
  </main>
</body>
</html>
```